SLA & Internet Advert

Advertise some of our key SLA services & Internet Connectivity services.
Service Level Agreement:
Unlimited Remote, Email, Helpdesk & Telephone Support.
Unlimited Service Calls
Support Hours Monday - Saturday 7am-10pm Sunday till 5pm
Free additional visits during ofsted periods
Free remote access to school server for staff members
Free mobile device management for tablet devices
Free Email&Webhosting Service
Remote support on every device in school allowing us to close 90% of tickets within 30 mins.
Service Level Agreement Package 1 - Includes all the above + 1 Site visit every 2 weeks £2,500 per annum
Service Level Agreement Package 2 - Includes all the above + 1 Site Visit every week £4,500 per annum
Service Level Agreement Package 3 - Includes all the above + 2 Site visits every week - £7,540 per annum
Internet Connectivity (medium/large Primary)
Managed Firewall
Managed Web filter & Safeguarding
User reporting portal/email reporting.
Main Internet Line 1000 mb/s download 100mb/s upload
Back up Internet Line 80mb/s download 20mb/s upload
100% uptime guaranteed.
£3000 per annum
Internet Connectivity (Small Primary School)
Managed Firewall
£2100 per annum
My website is https://www.lumora-net.co.uk if you need any further information like phone numbers / email address etc
Target Market(s)
Education
Look and feel
Each slider illustrates characteristics of the customer's brand and the style your logo design should communicate.

```html
<!DOCTYPE html>
<html lang="en">
<head>
<meta charset="utf-8">
<title>Lumora Net – SLA &amp; Internet Connectivity</title>
<link href="https://fonts.googleapis.com/css2?family=Montserrat:wght@400;500;600;700&display=swap" rel="stylesheet">
<style>
  :root{
    --stage:#262626;
    --paper:#ffffff;
    --orange:#f2844b;
    --blue:#0a72bd;
    --blue-dark:#0b5fa3;
    --pale:#dfe7f5;
    --ink:#1d1d1d;
    --text:#2e2e2e;
    --white:#ffffff;
  }
  *{box-sizing:border-box;margin:0;padding:0}
  html,body{width:1200px;height:1200px;overflow:hidden;background:var(--stage);font-family:"Montserrat",sans-serif}
  .flyer{position:absolute;left:244px;top:101px;width:711px;height:997px;background:var(--paper);overflow:hidden}

  .brand{position:absolute;top:30px;left:0;width:100%;display:flex;justify-content:center;align-items:center;gap:10px}
  .brand-mark{width:30px;height:30px;background:var(--blue);border-radius:4px}
  .brand-name{font-size:34px;font-weight:700;color:var(--blue);letter-spacing:1px}

  .rule{position:absolute;left:0;width:100%;background:var(--orange)}
  .rule-top{top:107px;height:6px}
  .rule-mid{top:372px;height:7px}

  .hero{position:absolute;top:117px;left:0;width:100%;height:253px;
    background:
      radial-gradient(ellipse 160px 140px at 140px 130px,rgba(120,70,110,.35),transparent 70%),
      radial-gradient(ellipse 180px 120px at 560px 90px,rgba(150,185,225,.45),transparent 70%),
      radial-gradient(ellipse 200px 110px at 480px 220px,rgba(40,80,150,.35),transparent 70%),
      linear-gradient(120deg,#5e93d2 0%,#4379bf 45%,#6d9dd6 100%)}
  .sla-title{position:absolute;top:163px;left:0;width:100%;text-align:center;color:var(--white);font-size:17px;font-weight:700}
  .sla-title span{border-bottom:2px solid var(--orange);padding-bottom:1px}
  .sla-list{position:absolute;top:193px;left:153px;list-style:none;color:var(--white);font-size:13px;font-weight:500}
  .sla-list li{height:19.5px;line-height:19.5px;padding-left:14px;position:relative}
  .sla-list li::before{content:"";position:absolute;left:0;top:6.5px;width:6px;height:6px;border:1.6px solid var(--orange);border-radius:50%;background:var(--white)}

  .promo{position:absolute;top:393px;left:0;width:100%;height:22px;background:var(--orange);color:var(--white);font-size:12px;font-weight:700;text-align:center;line-height:22px}
  .promo strong{color:var(--ink)}

  .package{position:absolute;top:429px;width:211px;height:106px;background:var(--blue);border-radius:13px;color:var(--white);text-align:center;padding-top:8px;box-shadow:0 2px 0 var(--blue-dark)}
  .package-1{left:25px}.package-2{left:250px}.package-3{left:475px}
  .package-label{font-size:12.5px;font-weight:700}
  .package-name{display:inline-block;margin:3px 0 4px;background:var(--orange);font-size:16px;font-weight:700;padding:0 8px;border-radius:0 8px 0 8px;line-height:20px}
  .package p{font-size:12.5px;font-weight:500;line-height:16px}

  .connect{position:absolute;top:549px;left:0;width:100%;height:397px;
    background:
      radial-gradient(ellipse 170px 90px at 150px 110px,rgba(255,255,255,.55),transparent 70%),
      radial-gradient(ellipse 220px 110px at 500px 130px,rgba(255,255,255,.5),transparent 70%),
      radial-gradient(ellipse 120px 120px at 260px 290px,rgba(255,255,255,.45),transparent 70%),
      radial-gradient(ellipse 90px 60px at 620px 320px,rgba(255,255,255,.5),transparent 70%),
      linear-gradient(180deg,var(--pale),#e6ecf7)}
  .footer-band{position:absolute;top:946px;left:0;width:100%;height:51px;background:var(--blue)}

  .offer{position:absolute;left:152px}
  .offer-1{top:558px}.offer-2{top:727px}
  .offer h2{font-size:16.5px;font-weight:700;color:var(--blue);padding-left:20px;position:relative;line-height:20px}
  .offer h2::before{content:"";position:absolute;left:0;top:7px;width:7px;height:7px;border-radius:50%;background:var(--orange)}
  .offer h2 span{border-bottom:2px solid var(--orange);padding-bottom:2px}
  .offer ul{list-style:none;margin:8px 0 0 24px;font-size:12.7px;color:var(--text);font-weight:400}
  .offer li{height:18.6px;line-height:18.6px;padding-left:18px;position:relative}
  .offer li::before{content:"";position:absolute;left:0;top:6px;width:6px;height:6px;border:1.6px solid var(--orange);border-radius:50%}

  .contact{position:absolute;left:122px;top:855px;width:473px;height:116px;background:var(--orange);border-radius:15px;box-shadow:0 3px 0 var(--white);color:var(--white);text-align:center;font-size:12.5px}
  .contact h3{display:inline-block;margin-top:7px;font-size:16px;font-weight:700;border:1.5px solid var(--white);border-radius:6px;padding:0 5px;line-height:20px}
  .contact .line{display:flex;justify-content:center;align-items:center;gap:4px;height:18px;margin-top:2px}
  .contact .line.pair{gap:36px}
  .contact .item{display:inline-flex;align-items:center;gap:4px}
  .contact svg{width:12px;height:12px}
  .socials{display:flex;justify-content:center;gap:8px;margin-top:3px}
  .socials span{width:14px;height:14px;border:1.2px solid var(--white);border-radius:50%}
</style>
</head>
<body>
<main class="flyer">
  <header class="brand">
    <span class="brand-mark"></span>
    <span class="brand-name">LUMORA NET</span>
  </header>

  <div class="rule rule-top"></div>
  <div class="hero" role="img" aria-label="Blue-tinted classroom photo: a pupil wearing a virtual reality headset in the foreground, classmates at laptops and a large gear shape on the wall behind"></div>
  <div class="sla-title"><span>Service Level Agreement:</span></div>
  <ul class="sla-list">
    <li>Unlimited Remote, Email, Helpdesk &amp; Telephone Support.</li>
    <li>Unlimited Service Calls</li>
    <li>Support Hours Monday - Saturday 7am-10pm Sunday till 5pm</li>
    <li>Free additional visits during ofsted periods</li>
    <li>Free remote access to school server for staff members</li>
    <li>Free mobile device management for tablet devices</li>
    <li>Free Email &amp; Web hosting Service</li>
  </ul>
  <div class="rule rule-mid"></div>

  <div class="promo">Remote support on every device in school allowing us to close <strong>90% of tickets</strong> within 30 mins.</div>

  <section class="package package-1">
    <div class="package-label">Service Level Agreement</div>
    <div class="package-name">Package 1</div>
    <p>- Includes all the above +</p>
    <p>1 Site visit every 2 weeks</p>
    <p>£2,500 per annum</p>
  </section>
  <section class="package package-2">
    <div class="package-label">Service Level Agreement</div>
    <div class="package-name">Package 2</div>
    <p>- Includes all the above +</p>
    <p>1 Site Visit every week</p>
    <p>£4,500 per annum</p>
  </section>
  <section class="package package-3">
    <div class="package-label">Service Level Agreement</div>
    <div class="package-name">Package 3</div>
    <p>- Includes all the above +</p>
    <p>2 Site visits every week -</p>
    <p>£7,540 per annum</p>
  </section>

  <div class="connect" role="img" aria-label="Faint white world map of the continents on a pale blue ground behind the connectivity offers"></div>
  <div class="footer-band"></div>

  <section class="offer offer-1">
    <h2><span>Internet Connectivity (medium/large Primary)</span></h2>
    <ul>
      <li>Managed Firewall</li>
      <li>Managed Web filter &amp; Safeguarding</li>
      <li>User reporting portal/email reporting</li>
      <li>Main Internet Line 1000 mb/s download 100mb/s upload</li>
      <li>Back up Internet Line 80mb/s download 20mb/s upload</li>
      <li>100% uptime guaranteed</li>
      <li>£3000 per annum</li>
    </ul>
  </section>
  <section class="offer offer-2">
    <h2><span>Internet Connectivity (Small Primary School)</span></h2>
    <ul>
      <li>Managed Firewall</li>
      <li>Managed Web filter &amp; Safeguarding</li>
      <li>User reporting portal/email reporting</li>
      <li>Main Internet Line 1000 mb/s download 100mb/s upload</li>
      <li>£2100 per annum</li>
    </ul>
  </section>

  <section class="contact">
    <h3>Contact us:</h3>
    <div class="line">
      <span class="item"><svg viewBox="0 0 12 12"><circle cx="6" cy="6" r="5" fill="none" stroke="#fff" stroke-width="1"/><path d="M1 6h10M6 1c-2 2-2 8 0 10M6 1c2 2 2 8 0 10" fill="none" stroke="#fff" stroke-width=".8"/></svg>www.lumora-net.co.uk</span>
    </div>
    <div class="line pair">
      <span class="item"><svg viewBox="0 0 12 12"><circle cx="6" cy="6" r="5.4" fill="none" stroke="#fff" stroke-width="1"/><path d="M4 3.2l1 1.6-.6.8c.4.9 1.1 1.6 2 2l.8-.6 1.6 1-.6 1.2c-2.4-.3-4.4-2.3-4.7-4.7z" fill="#fff"/></svg>01632 960 418</span>
      <span class="item"><svg viewBox="0 0 12 12"><circle cx="6" cy="6" r="5.4" fill="none" stroke="#fff" stroke-width="1"/><rect x="3" y="4" width="6" height="4.2" fill="none" stroke="#fff" stroke-width=".8"/><path d="M3 4l3 2.4L9 4" fill="none" stroke="#fff" stroke-width=".8"/></svg>info@lumora-net.co.uk</span>
    </div>
    <div class="line">
      <span class="item"><svg viewBox="0 0 12 12"><circle cx="6" cy="6" r="5.4" fill="none" stroke="#fff" stroke-width="1"/><path d="M6 2.6a2.2 2.2 0 0 1 2.2 2.2C8.2 6.4 6 9 6 9S3.8 6.4 3.8 4.8A2.2 2.2 0 0 1 6 2.6z" fill="none" stroke="#fff" stroke-width=".8"/></svg>Lumora Net LTD Harbour House, Alder Street Kelby Westshire KB4 7QX</span>
    </div>
    <div class="socials"><span></span><span></span><span></span></div>
  </section>
</main>
</body>
</html>
```